「特殊詐欺」次はあなたがターゲットをタイトルに
「特殊詐欺」撃退機設置の【写真と図解】掲載と悲痛な「被害者の体験記事」を掲載して皆さんに読んでいただいて「特殊詐欺」」の被害者にならないようにの思いを伝える本にしたい。
警官名乗る詐欺急増
詐欺の電話は非通知です。
[通話警備団 改204]
被害者の体験記事(1)
息子は会社をクビになるかもしれないと思い
道路上で男にお金を渡してしまったのです。
騙されたお金は戻って来ません。
被害者の体験記事(2)
キャッシュカードを取り替えないと
被害者の体験記事(3)
犯罪は人の良心を逆手に取る

選んだ理由:デザインが目を引くものを感じました。文字がハッキリ読み取れる所や色彩も良かった。

他にもたくさんの方にご提案して頂いてありがとうございました。
これからもまたご提案をお願いいたします。
本当にありがとうございました。

```html
<!DOCTYPE html>
<html lang="ja">
<head>
<meta charset="UTF-8">
<title>特殊詐欺 次はあなたがターゲット</title>
<link rel="stylesheet" href="https://fonts.googleapis.com/css2?family=Dela+Gothic+One&family=M+PLUS+1p:wght@800;900&display=swap">
<style>
  :root {
    --cream: #fdf8d6;
    --title-gold: #f6b40e;
    --navy: #1c2b5a;
    --red: #e2231a;
    --green: #7cc242;
    --yellow: #ffe23a;
    --pink: #f39aa0;
    --white: #ffffff;
    --illust-top: #cfe3f2;
    --illust-bottom: #f3d9b8;
  }
  * { margin: 0; padding: 0; box-sizing: border-box; }
  html, body { width: 749px; height: 1200px; overflow: hidden; }
  body {
    background: var(--cream);
    font-family: "M PLUS 1p", sans-serif;
    position: relative;
  }
  .cover { position: absolute; inset: 0; }
  .main-title {
    position: absolute; top: 18px; left: 0; width: 100%;
    text-align: center;
    font-family: "Dela Gothic One", sans-serif;
    font-size: 118px; line-height: 1.1;
    color: var(--title-gold);
    -webkit-text-stroke: 7px var(--navy);
    paint-order: stroke fill;
    letter-spacing: 4px;
  }
  .bubble-frame { position: absolute; top: 130px; left: 70px; width: 610px; height: 250px; }
  .exclaim { position: absolute; }
  .exclaim.left { top: 220px; left: 90px; }
  .exclaim.right { top: 190px; left: 600px; }
  .next-badge {
    position: absolute; top: 185px; left: 195px;
    width: 92px; height: 58px; border-radius: 50%;
    background: var(--yellow); border: 3px solid var(--navy);
    color: var(--red); font-weight: 900; font-size: 30px;
    display: flex; align-items: center; justify-content: center;
    transform: rotate(-8deg);
  }
  .headline {
    position: absolute; left: 0; width: 100%; text-align: center;
    font-family: "Dela Gothic One", sans-serif;
    color: var(--navy);
  }
  .headline.line-you { top: 158px; padding-left: 150px; font-size: 76px; }
  .headline.line-target { top: 238px; padding-left: 60px; font-size: 92px; }
  .illustration {
    position: absolute; top: 370px; left: 75px; width: 600px; height: 450px;
    border-radius: 40% 45% 30% 30%;
    background: linear-gradient(180deg, var(--illust-top), var(--illust-bottom));
  }
  .prevent-burst {
    position: absolute; top: 815px; left: 115px;
    padding: 10px 26px;
    background: var(--yellow);
    border-radius: 30px;
    color: var(--red); font-weight: 900; font-size: 34px;
    transform: rotate(-6deg);
  }
  .feature-box {
    position: absolute; top: 885px; left: 62px; width: 625px; height: 140px;
    background: var(--white);
    padding: 14px 10px;
    color: var(--navy); font-weight: 900;
    display: flex; flex-direction: column; justify-content: space-around;
  }
  .feature-line { white-space: nowrap; line-height: 1.3; letter-spacing: -1px; }
  .feature-line.one { font-size: 22px; }
  .feature-line.two { font-size: 28px; }
  .accent { color: var(--red); }
  .lead-big { font-size: 31px; }
  .tag-small { font-size: 15px; }
  .end-big { font-size: 28px; }
  .accent-big { font-size: 32px; }
  .tail-small { font-size: 18px; }
  .contents-band {
    position: absolute; top: 1058px; left: 70px; width: 610px; height: 122px;
    background: var(--pink);
    display: flex; flex-direction: column; justify-content: center; align-items: center;
    color: var(--yellow); font-weight: 900; font-size: 27px; line-height: 1.5;
    white-space: nowrap;
    -webkit-text-stroke: 1px var(--red);
  }
</style>
</head>
<body>
<div class="cover">
  <h1 class="main-title">特殊詐欺</h1>

  <svg class="bubble-frame" viewBox="0 0 610 250" aria-hidden="true">
    <path d="M60 40 Q300 -10 560 30 Q610 120 560 220 Q300 260 60 225 Q0 130 60 40 Z"
          fill="#ffffff" stroke="#1c2b5a" stroke-width="4"/>
  </svg>

  <svg class="exclaim left" width="50" height="110" viewBox="0 0 50 110" aria-hidden="true">
    <path d="M8 5 L38 2 L32 72 L16 72 Z" fill="#7cc242" transform="rotate(-10 25 50)"/>
    <circle cx="22" cy="92" r="11" fill="#7cc242"/>
  </svg>
  <svg class="exclaim right" width="56" height="140" viewBox="0 0 56 140" aria-hidden="true">
    <path d="M10 5 L46 2 L38 95 L20 95 Z" fill="#7cc242" transform="rotate(10 28 60)"/>
    <circle cx="34" cy="120" r="13" fill="#7cc242"/>
  </svg>

  <div class="next-badge">次は</div>
  <p class="headline line-you">あなたが</p>
  <p class="headline line-target">ターゲット</p>

  <div class="illustration" role="img" aria-label="サングラスの詐欺師が電話をかけ、高齢の女性が受話器を持って驚いている場面のイラスト"></div>

  <p class="prevent-burst">未然に防げる!</p>

  <div class="feature-box">
    <p class="feature-line one"><span class="accent lead-big">「録音します<span class="tag-small">メッセージ</span>」</span>が「サギ」を防ぐ<span class="end-big">撃退機!</span></p>
    <p class="feature-line two">補助金で<span class="accent accent-big">「撃退機付け」</span><span class="tail-small">「サギ電話」を断ち切った!</span></p>
  </div>

  <div class="contents-band">
    <p>「特殊詐欺」撃退機設置の【写真と図解】、</p>
    <p>悲痛な「被害者の体験記事」掲載</p>
  </div>
</div>
</body>
</html>
```